Visit card

Industry/Entity Type

Health Care

Contact Information for Business Card

O VITAL SYSTEMIQUE
Odile Ferrand - chef de Projet

Requirements
Must have
• 318 Rue des Tilleuls Verts 47150 VERNAUBOURG Tel: 33 (0) 487 204 615 Mobile: 06 42 93 17 58 Web: www.cliniqorvane.example Contact: o.ferrand@o-vitalsystemique.example
Should not have
• Respect for color

```html
<!DOCTYPE html>
<html lang="fr">
<head>
<meta charset="utf-8">
<title>O VITAL SYSTEMIQUE – Carte de visite</title>
<link rel="stylesheet" href="https://fonts.googleapis.com/css2?family=Lato:wght@400;700;900&display=swap">
<style>
  :root {
    --page-bg: #e7e2dc;
    --card-bg: #4b4947;
    --card-edge: #5d5a57;
    --text-main: #d6cfc6;
    --text-soft: #cbc3b9;
    --brand-red: #cf2a2c;
    --disc: #d9d2c8;
  }
  * { margin: 0; padding: 0; box-sizing: border-box; }
  html, body {
    width: 1200px;
    height: 1047px;
    overflow: hidden;
    background: var(--page-bg);
    font-family: "Lato", sans-serif;
  }
  .card {
    position: absolute;
    left: 151px;
    top: 291px;
    width: 944px;
    height: 513px;
    border-radius: 20px;
    background: var(--card-bg);
    border: 1px solid var(--card-edge);
    overflow: hidden;
  }
  .brand {
    position: absolute;
    left: 39px;
    top: 25px;
    height: 112px;
    display: flex;
    align-items: center;
    gap: 35px;
  }
  .brand-dot {
    width: 112px;
    height: 112px;
    border-radius: 50%;
    background: var(--disc);
  }
  .brand-name {
    font-weight: 900;
    font-size: 26px;
    letter-spacing: 1px;
    color: var(--brand-red);
  }
  .brand-disc {
    position: absolute;
    left: 444px;
    top: 20px;
    width: 468px;
    height: 468px;
    border-radius: 50%;
    background: var(--disc);
  }
  .person {
    position: absolute;
    left: 38px;
    top: 180px;
  }
  .person-name {
    font-size: 32px;
    font-weight: 400;
    letter-spacing: 0.5px;
    color: var(--text-main);
    line-height: 40px;
  }
  .person-role {
    font-size: 20px;
    line-height: 30px;
    color: var(--text-soft);
  }
  .address {
    position: absolute;
    left: 38px;
    top: 280px;
    font-size: 21px;
    line-height: 31px;
    color: var(--text-soft);
    font-style: normal;
  }
  .contacts {
    position: absolute;
    left: 36px;
    top: 362px;
    list-style: none;
  }
  .contacts li {
    display: flex;
    align-items: center;
    gap: 10px;
    height: 31px;
    font-size: 20.5px;
    color: var(--text-soft);
  }
  .contacts li.small { font-size: 19.5px; }
  .contacts svg {
    width: 16px;
    height: 16px;
    fill: none;
    stroke: var(--text-soft);
    stroke-width: 1.6;
    flex: none;
  }
</style>
</head>
<body>
  <section class="card">
    <div class="brand-disc"></div>

    <header class="brand">
      <div class="brand-dot"></div>
      <span class="brand-name">O VITAL SYSTEMIQUE</span>
    </header>

    <div class="person">
      <h1 class="person-name">ODILE FERRAND</h1>
      <p class="person-role">Chef de Projet</p>
    </div>

    <address class="address">
      318 Rue des Tilleuls Verts<br>
      47150 VERNAUBOURG
    </address>

    <ul class="contacts">
      <li>
        <svg viewBox="0 0 16 16"><path d="M3 1.5l3 .5 1 3-1.7 1.3a8 8 0 0 0 4.4 4.4L11 9l3 1 .5 3-1.5 1.5C7 14.5 1.5 9 1.5 3z"/></svg>
        +33 (0) 487 204 615
      </li>
      <li>
        <svg viewBox="0 0 16 16"><rect x="4" y="1.5" width="8" height="13" rx="1.5"/><path d="M7 12.3h2"/></svg>
        06 42 93 17 58
      </li>
      <li class="small">
        <svg viewBox="0 0 16 16"><circle cx="8" cy="8" r="6.5"/><path d="M1.5 8h13M8 1.5c-3 3.5-3 9.5 0 13M8 1.5c3 3.5 3 9.5 0 13"/></svg>
        www.cliniqorvane.example
      </li>
      <li class="small">
        <svg viewBox="0 0 16 16"><rect x="1.5" y="3.5" width="13" height="9" rx="1"/><path d="M1.5 4l6.5 5 6.5-5"/></svg>
        o.ferrand@o-vitalsystemique.example
      </li>
    </ul>
  </section>
</body>
</html>
```